Design a New Site for a very cool Watch

We have the overall design element of the website and the banners in the PSD file. We need someone to finish our design in PSD and than convert to HTML. We have included the instructions, PSD file, images and all text.

We currently use Hubspot to host and make changes to our site. The entire design aspect is complete so all we need is some minor changes and additions within the photoshop design and than the coding into HTML.

Please only sign up if you understand photoshop and HTML conversion

Here is the DropBox link to the files
https://www.filemarrow.com/s/qk7vbn3lwpe9tdx/Velqor%20Site.zip
Updates

We have the basic design concept in Photoshop.  We just need someone who can complete some changes, make some additions and convert to HTML

Target Market(s)

Watch Buyers

Requirements
Must have
• Must look like a professional luxury brand

Our brand colors are very basic with Black, White and Grey can be used

```html
<!DOCTYPE html>
<html lang="en">
<head>
<meta charset="utf-8">
<title>Velqor &amp; Co.</title>
<link href="https://fonts.googleapis.com/css2?family=Open+Sans:wght@400;600;700&family=Arimo:wght@400;700&display=swap" rel="stylesheet">
<style>
:root{
  --ink:#222;
  --dark:#2f2f2f;
  --nav:#333;
  --muted:#555;
  --grey-bar:#a9a9a9;
  --rule:#d4d4d4;
  --accent:#e8141b;
  --card-bg:#fdf0f0;
  --card-line:#ecdcdc;
  --section-bg:#fdf8f8;
  --white:#fff;
}
*{margin:0;padding:0;box-sizing:border-box}
html,body{width:1024px;height:1200px;overflow:hidden;background:var(--white)}
body{position:relative;font-family:"Open Sans",sans-serif;color:var(--ink)}
.abs{position:absolute}
.top-strip{left:0;top:0;width:1024px;height:4px;background:var(--dark)}
.util-nav{left:82px;top:11px;font-size:10px;display:flex;gap:18px}
.util-right{right:68px;top:11px;font-family:"Arimo",sans-serif;font-size:10px;display:flex;gap:10px;align-items:center}
.util-right .shop{color:var(--accent)}
.util-right .sep{width:1px;height:12px;background:#999}
.brand{left:0;width:1024px;top:48px;display:flex;justify-content:center;align-items:center;gap:10px}
.brand-mark{width:22px;height:22px;border:1.5px solid var(--ink)}
.brand-name{font-size:19px;font-weight:400;letter-spacing:1px}
.dash{left:0;width:1024px;border-top:1px dashed var(--rule)}
.main-nav{left:0;top:112px;width:1024px;height:30px;background:var(--nav)}
.main-nav span{position:absolute;top:9px;color:var(--white);font-family:"Arimo",sans-serif;font-size:10.5px}
.main-nav svg{position:absolute;top:10px}
.search{left:740px;top:112px;width:180px;height:30px;background:#4a4a4a;color:#999;font-family:"Arimo",sans-serif;font-size:10.5px;padding:9px 14px}
.search-btn{left:920px;top:112px;width:30px;height:30px;background:#1d1d1d}
.hero{left:0;top:173px;width:1024px;height:321px;background:#000;overflow:hidden}
.hero-watch{left:0;top:0;width:440px;height:321px;background:radial-gradient(ellipse at 45% 45%,#d8dadb 0%,#a9acae 35%,#4b4b4b 65%,#0b0b0b 100%)}
.hero-moon{left:683px;top:27px;width:254px;height:254px;border-radius:50%;background:radial-gradient(circle at 45% 40%,#f3a0a4,#e06b72 70%,#c9535a)}
.hero-kicker{left:506px;top:122px;color:var(--white);font-size:15px;font-weight:600;letter-spacing:.5px}
.hero-title{left:506px;top:147px;color:var(--white);font-size:17px;font-weight:700;letter-spacing:1px}
.hero-note{left:506px;top:191px;color:var(--accent);font-family:"Arimo",sans-serif;font-size:10px}
.hero-arrow{top:136px;width:40px;height:39px;background:rgba(40,40,40,.85)}
.hero-dots{left:442px;top:290px;display:flex;gap:6px}
.hero-dots i{width:9px;height:9px;border-radius:50%;background:#888}
.hero-dots i.on{background:var(--white)}
.hero-base{left:0;top:494px;width:1024px;height:7px;background:#5a5a5a}
.lower-bg{left:0;top:770px;width:1024px;height:325px;background:var(--section-bg)}
.card{top:551px;width:203px;height:233px;background:var(--card-bg);border:1px solid var(--card-line);border-bottom:none}
.card::after{content:"";position:absolute;left:-1px;right:-1px;bottom:0;height:7px;background:var(--grey-bar)}
.card-icon{position:absolute;left:53px;top:34px;width:97px;height:97px;border-radius:50%;background:var(--white);border:1px solid #ddd;display:flex;align-items:center;justify-content:center}
.card-label{position:absolute;left:0;width:100%;top:160px;text-align:center;font-size:11px;line-height:17px;letter-spacing:.3px}
.section-rule{left:0;top:829px;width:1024px;border-top:1px solid #e5dede}
.about-title{left:73px;top:851px;font-size:12.5px;letter-spacing:.5px}
.about-photo{left:73px;top:888px;width:203px;height:103px;background:linear-gradient(90deg,#6f6354,#3f3934 55%,#1e1b1a)}
.about-text{left:298px;top:894px;width:192px;font-family:"Arimo",sans-serif;font-size:10px;line-height:13.8px;color:var(--muted)}
.about-text a{color:var(--accent);text-decoration:none}
.keep{left:530px;top:885px;width:190px;text-align:center}
.keep-title{font-size:17px;font-weight:600;color:#444;margin-top:6px}
.social{left:746px;top:934px;width:195px;height:38px;background:#eeeaea;display:flex;align-items:center;justify-content:space-around;padding:0 8px}
.social i{width:26px;height:26px;border-radius:50%;background:#c4c4c4}
.bar{top:1033px;height:7px;background:var(--grey-bar)}
.footer{left:0;top:1112px;width:1024px;height:88px;background:var(--dark);color:var(--white);font-family:"Arimo",sans-serif}
.footer-links{position:absolute;top:31px;width:100%;display:flex;justify-content:center;gap:28px;font-size:10.5px;letter-spacing:.3px}
.copyright{position:absolute;top:57px;width:100%;text-align:center;font-size:10px;color:#ccc}
</style>
</head>
<body>
<div class="abs top-strip"></div>
<nav class="abs util-nav"><span>My Account</span><span>Collection</span><span>Lifestyle</span><span>Shop now</span></nav>
<div class="abs util-right"><span class="shop">shop.velqor.com</span><span class="sep"></span><span>Sign in - Register</span></div>

<header class="abs brand"><span class="brand-mark"></span><span class="brand-name">VELQOR &amp; CO.</span></header>
<div class="abs dash" style="top:97px"></div>

<nav class="abs main-nav">
  <span style="left:83px">HOME</span>
  <span style="left:137px">PRODUCTS</span><svg style="left:199px" width="6" height="10"><path d="M1 1l4 4-4 4" stroke="#fff" stroke-width="1.8" fill="none"/></svg>
  <span style="left:232px">ARTICLES</span><svg style="left:288px" width="6" height="10"><path d="M1 1l4 4-4 4" stroke="#fff" stroke-width="1.8" fill="none"/></svg>
  <span style="left:325px">PHOTO GALLERY</span><svg style="left:412px" width="6" height="10"><path d="M1 1l4 4-4 4" stroke="#fff" stroke-width="1.8" fill="none"/></svg>
  <span style="left:449px">BLOG</span>
  <span style="left:501px">CONTACT</span>
</nav>
<div class="abs search">SEARCH</div>
<div class="abs search-btn"><svg width="30" height="30"><circle cx="13" cy="13" r="4.5" stroke="#fff" stroke-width="2" fill="none"/><path d="M16 16l6 6" stroke="#fff" stroke-width="3"/></svg></div>
<div class="abs dash" style="top:157px"></div>

<section class="abs hero">
  <div class="abs hero-watch" role="img" aria-label="Close-up photo of a white square ladies' watch with floating pink sapphires"></div>
  <div class="abs hero-moon" role="img" aria-label="Photo of a pink full moon"></div>
  <div class="abs hero-kicker">WOMAN’S LIMITED EDITION</div>
  <div class="abs hero-title">FLOATING PINK SAPPHIRE LYRA WATCH</div>
  <div class="abs hero-note">Limited to 200 pieces Worldwide</div>
  <div class="abs hero-arrow" style="left:57px"><svg width="40" height="39"><path d="M22 16l-3 3.5 3 3.5" stroke="#ddd" stroke-width="1.3" fill="none"/></svg></div>
  <div class="abs hero-arrow" style="left:927px"><svg width="40" height="39"><path d="M19 16l3 3.5-3 3.5" stroke="#ddd" stroke-width="1.3" fill="none"/></svg></div>
  <div class="abs hero-dots"><i></i><i></i><i></i><i class="on"></i><i></i></div>
</section>
<div class="abs hero-base"></div>

<div class="abs lower-bg"></div>

<article class="abs card" style="left:73px">
  <div class="card-icon"><svg width="60" height="60" fill="#777"><path d="M34 14l5 12 13 1-10 8 3 13-11-7-11 7 3-13-10-8 13-1z"/><path d="M14 6l2 6 6 0-5 4 2 6-5-4-5 4 2-6-5-4 6 0z"/><path d="M43 8l1.5 3.5 3.5.3-2.7 2.3 .9 3.6-3.2-2-3.2 2 .9-3.6-2.7-2.3 3.5-.3z"/></svg></div>
  <div class="card-label">THE LYRA STORY</div>
</article>
<article class="abs card" style="left:298px">
  <div class="card-icon"><svg width="64" height="50"><rect x="10" y="4" width="44" height="32" rx="2" fill="none" stroke="#777" stroke-width="3"/><text x="32" y="23" font-family="Open Sans,sans-serif" font-size="7" fill="#777" text-anchor="middle">REGISTER</text><path d="M2 38h60l-4 7H6z" fill="#777"/></svg></div>
  <div class="card-label">REGISTER YOUR<br>WATCH</div>
</article>
<article class="abs card" style="left:524px">
  <div class="card-icon"><svg width="70" height="60" fill="none" stroke="#777" stroke-width="3"><rect x="10" y="4" width="14" height="10" rx="2"/><rect x="10" y="46" width="14" height="10" rx="2"/><circle cx="17" cy="30" r="15"/><path d="M17 30l-5 6M17 30v-8" stroke-width="2"/><circle cx="48" cy="20" r="6" stroke-width="5" stroke-dasharray="3 2"/><circle cx="54" cy="42" r="5" stroke-width="4" stroke-dasharray="3 2"/></svg></div>
  <div class="card-label">REPAIR, MAINTENANCE<br>&amp; WARRENTY INFO</div>
</article>
<article class="abs card" style="left:748px">
  <div class="card-icon"><svg width="72" height="46"><path d="M14 14l52 6-4 24-52-6-6-14z" fill="#666"/><circle cx="12" cy="24" r="3" fill="#fff"/><text x="40" y="34" font-family="Open Sans,sans-serif" font-weight="700" font-style="italic" font-size="14" fill="#fff" text-anchor="middle" transform="rotate(8 40 30)">New</text></svg></div>
  <div class="card-label">REGISTER TO FIND OUT ABOUT<br>NEW WATCH COLECTIONS</div>
</article>

<div class="abs section-rule"></div>
<h2 class="abs about-title" style="font-weight:400">VELQOR &amp; CO</h2>
<div class="abs about-photo" role="img" aria-label="Photo of a woman standing beside a brand promotional poster"></div>
<p class="abs about-text">Lorem ipsum dolor sit amet, consectetur adipisicing elit, sed do eiusmod tempor incididunt ut labore et dolore magna aliqua. Ut enim ad minim veniam, quis nostrud exercitation ullamco laboris nisi ut aliquip ex ea commodo consequat.<br><a href="#">www.velqor.com</a></p>

<div class="abs keep">
  <svg width="70" height="62"><path d="M8 34a27 20 0 0 0 54 0a27 20 0 0 1-54 0z" fill="none"/><path d="M6 32c0 14 13 24 29 24s29-10 29-24c-4 8-15 14-29 14S10 40 6 32z" fill="#666"/><rect x="23" y="14" width="24" height="18" fill="#fff" stroke="#666" stroke-width="2.5"/><path d="M23 14l12 10 12-10" fill="none" stroke="#666" stroke-width="2.5"/><path d="M23 14l12-9 12 9" fill="none" stroke="#666" stroke-width="2.5"/></svg>
  <div class="keep-title">KEEP IN TOUCH</div>
</div>
<div class="abs social" aria-label="Social links"><i></i><i></i><i></i><i></i><i></i></div>

<div class="abs bar" style="left:73px;width:427px"></div>
<div class="abs bar" style="left:524px;width:427px"></div>
<div class="abs dash" style="top:1095px"></div>

<footer class="abs footer">
  <div class="footer-links"><span>VELQOR &amp; COMPANY</span><span>CONTACT US</span><span>TERMS OF SERVICE</span><span>REFUND POLICY</span><span>PRIVACY POLICY</span></div>
  <div class="copyright">Copyright © 2013 Velqor &amp; Co<sup style="font-size:7px">TM</sup></div>
</footer>
</body>
</html>
```